Perfume Oil manufacturing and distribution company needs an emotion inspiring Wordpress Design

Must be Wordpress Design
Beautiful website needed for a company that manufactures and distributes scents that fragrance products from fine fragrances to personal care and household products. Please refer to attached file (namely "brief" for detailed explanation of our company, product and design requirements)

Website must be beautiful, and not too cluttered.

Must be coded for use in WordPress after design phase

remember not to flood website with pictures of perfumes and perfume bottles, this website is meant to inspire emotion...looking at the big fragrance brands (Valdoret and Morvaleth) one will not see pictures of perfume bottles etc. The site is all about emotion and smell and the senses.
Keep this in mind when submitting designs.

The site must captivate and inspire emotion with beautiful visuals.

the website must be about how one feels when surrounded by a beautiful smell, how one feels confident wearing a good scent. how freshly baked break reminds you of your grandmas house, or how a scent can remind of a seductive encounter, or a memory of fun times with friends out on the town, or as simple as the smell of a good cup of coffee or a rose to inspire a new days happenings.

all this emotion and feeling must be tied into the fact that Aroma Nest makes these moments through great smells. Which we supply to manufacturers of these great end products. whether it is a fine fragrance, a lotion, a car fragrance or a home spray. We scent the world around us.

try not to look too much at our existing website as this is outdated and the company has changed much since then, refer to this and the attached brief

Target Market(s)

small to medium businesses who manufacture products that need to be fragranced. whether these products be prestigious fine fragrances, daily personal care products or home care products, we make the fragrances that make these products beautiful.

Industry/Entity Type

Perfume

Coding

Coded - Design and coding required

Number of Pages Required

5+ page

Font styles to use
Serif
Sans Serif

Colors

Designer to choose colors to be used in the design.

Requirements
Must have
• must have full page header that captivates audience and inspires emotion (through a video or powerful imagery)
• Smell is a powerful emotion trigger and since a computer screen can not produce smell we will need to engage emotion through beautiful imagery and or video and beautiful design on the website. (refer to attached "brief" for more details)
• Must be coded for use in WordPress ONLY after design phase
• site must work well and look great on mobile since most of our audience use mobile to access our site.
Should not have
• too many pictures of perfume packaging and actual products, looking at the big fragrance manufacturers (Valdoret, Morvaleth, KTB) one will not see pictures of perfume bottles and packaging. This is very important as the website is more to inspire emotion and give a sense of how fragrance and perfume makes one feel.
• The site must captivate and inspire emotion with beautiful visuals.

```html
<!DOCTYPE html>
<html lang="en">
<head>
<meta charset="UTF-8">
<title>Aroma Nest — Master Perfumers</title>
<link href="https://fonts.googleapis.com/css2?family=Cormorant+Garamond:wght@500&family=Josefin+Sans:wght@400;600&display=swap" rel="stylesheet">
<style>
  :root {
    --bg: #2a211d;
    --gold: #f6dc97;
    --gold-soft: #efd590;
    --ghost: rgba(255, 236, 190, 0.055);
    --skin-light: #d9a88a;
    --skin-mid: #b57a5c;
    --skin-dark: #5a3a2c;
  }
  * { margin: 0; padding: 0; box-sizing: border-box; }
  html, body { width: 1200px; height: 682px; overflow: hidden; background: var(--bg); }
  .hero {
    position: relative;
    width: 1200px;
    height: 682px;
    background: var(--bg);
    overflow: hidden;
    font-family: "Cormorant Garamond", Georgia, serif;
    color: var(--gold);
  }
  .hero__watermark {
    position: absolute;
    left: 0; top: 0;
    width: 1200px; height: 682px;
  }
  .hero__watermark text {
    font-family: "Cormorant Garamond", Georgia, serif;
    font-size: 372px;
    fill: var(--ghost);
  }
  .hero__photo {
    position: absolute;
    left: 0; top: 0;
    width: 720px; height: 682px;
    background:
      radial-gradient(ellipse 45% 40% at 42% 38%, var(--skin-light) 0%, var(--skin-mid) 55%, transparent 100%),
      radial-gradient(ellipse 55% 30% at 55% 85%, var(--skin-mid) 0%, var(--skin-dark) 60%, transparent 100%),
      linear-gradient(90deg, var(--skin-dark) 0%, rgba(90,58,44,0.6) 60%, transparent 100%);
  }
  .nav {
    position: absolute;
    top: 28px;
    left: 0;
    width: 1200px;
    height: 24px;
  }
  .nav__link {
    position: absolute;
    top: 0;
    font-size: 15px;
    line-height: 24px;
    color: var(--gold);
    text-decoration: none;
    white-space: nowrap;
  }
  .brand {
    position: absolute;
    left: 846px;
    top: 174px;
    transform: translateX(-50%);
    text-align: center;
    font-family: "Josefin Sans", Arial, sans-serif;
    color: var(--gold);
  }
  .brand__dot {
    width: 46px; height: 46px;
    border-radius: 50%;
    background: var(--gold);
    margin: 0 auto 14px;
  }
  .brand__name {
    font-size: 38px;
    font-weight: 600;
    line-height: 40px;
    white-space: nowrap;
  }
  .brand__tagline {
    font-size: 16px;
    font-weight: 400;
    line-height: 20px;
    margin-top: 2px;
  }
  .hero__title {
    position: absolute;
    left: 548px;
    top: 308px;
    width: 626px;
    font-size: 58px;
    font-weight: 500;
    line-height: 74px;
    white-space: nowrap;
    text-align: center;
  }
  .hero__subtitle {
    position: absolute;
    left: 620px;
    top: 388px;
    width: 480px;
    text-align: center;
    font-family: "Josefin Sans", Arial, sans-serif;
    font-size: 21px;
    letter-spacing: 6.5px;
    line-height: 28px;
    color: var(--gold);
    white-space: nowrap;
  }
  .hero__cta {
    position: absolute;
    left: 766px;
    top: 447px;
    width: 172px;
    height: 46px;
    border: 1px solid var(--gold-soft);
    font-family: "Josefin Sans", Arial, sans-serif;
    font-size: 16px;
    line-height: 46px;
    text-align: center;
    color: var(--gold);
    text-decoration: none;
  }
</style>
</head>
<body>
<section class="hero">
  <svg class="hero__watermark" viewBox="0 0 1200 682" aria-hidden="true">
    <text x="24" y="372" textLength="1132" lengthAdjust="spacing">SCENT</text>
  </svg>

  <div class="hero__photo" role="img" aria-label="Woman with closed eyes enjoying a fragrance, holding a small dark scent jar in her palm"></div>

  <nav class="nav">
    <a class="nav__link" href="#" style="left:531px">About</a>
    <a class="nav__link" href="#" style="left:604px">Our Services</a>
    <a class="nav__link" href="#" style="left:714px">Our Products</a>
    <a class="nav__link" href="#" style="left:821px">Blog</a>
    <a class="nav__link" href="#" style="left:885px">Contact us</a>
    <a class="nav__link" href="#" style="left:980px">Online Training</a>
    <a class="nav__link" href="#" style="left:1109px">Careers</a>
  </nav>

  <div class="brand">
    <div class="brand__dot"></div>
    <div class="brand__name">Aroma Nest</div>
    <div class="brand__tagline">Master Perfumers</div>
  </div>

  <h1 class="hero__title">Best in Fragrance Industry</h1>
  <p class="hero__subtitle">FEEL THE SCENT YOU WANT</p>
  <a class="hero__cta" href="#">ORDER</a>
</section>
</body>
</html>
```